College Social website needs a SIMPLE chart design

We need a simple one page website. The website is called "Fim-Bosk" a phonetic spelling of the word collage. The site allows users to gain up to date information on the nightlife and social scene of the campus. The site must be able to easily convey several key pieces of information; some type of grid/chart would work well.

This includes:
primary information:
-The name of the bar (about 9 bars on campus)
-The length of the line
-Guy/Girl ratio
-If there is cover (admittance fee) to enter the bar

secondary information:
-how packed/full the bar is
-if there is police raiding the bar
-a way to show more information including drink specials

would prefer a design similar to this page except more colorful/playful/fun: http://m.vantorelq.com/results.php

Some stylistic tips - the name of the service is called fim bosk. a phonetic spelling of collage (http://en.quorbinet.org/wiki/Collage). it doesnt need to look like a rainbow, just be exciting, engaging, and vivid.

look at this page for reference: http://www.plimvadee.com/blog/flat-ui-design-showcase/

other than the bar name and drink specials, everything should be presented graphically. All the bar stats are approximations and rough estimates, so you must find a way to present the information as relatives. historical information is not relevant. only the real time stats need to be included. here is a sample:

Bar name: Sample bar
guy/girl ratio: 70/30
line length: short
admittance fee: yes
bar attendance: near full
police raid: no
drink specials:
WINE NIGHT!
$8 BOTTLES OF GALLOWMERE WINE
$8 BOTTLES OF CHAMPAGNE
$2 TRESK PALE BOTTLES
$2 WELLS

Target Market(s)

target market for the site is 18-21 year olds in college.

Industry/Entity Type

College

Requirements
Must have
• the design MUST be mobile friendly. keep it simple. a flat design would be preferred.
the information must be conveyed in the form of symbols/icons. for instance, a pie chart to show guy/girl ratio.

```html
<!DOCTYPE html>
<html lang="en">
<head>
<meta charset="utf-8">
<title>Fim-Bosk – Find bars near you</title>
<link rel="stylesheet" href="https://fonts.googleapis.com/css2?family=Source+Sans+3:wght@400;600;700&display=swap">
<style>
  :root {
    --page-bg: #f2f2f2;
    --panel-bg: #ffffff;
    --panel-border: #d9d9d9;
    --brand-blue: #2a9fd6;
    --brand-blue-light: #5fb8e3;
    --search-blue: #4dbde0;
    --search-blue-pale: #bde6f3;
    --teal: #14a9c8;
    --orange: #f7744f;
    --sky: #4fd0ea;
    --red: #c75a5a;
    --ink: #444444;
    --ink-soft: #777777;
    --ink-faint: #a6a6a6;
    --ratio-core: #555555;
    --nav-active: #e6f5fb;
    --social-1: #5cc2ec;
    --social-2: #3c5a99;
    --social-3: #ea4c89;
  }
  * { box-sizing: border-box; margin: 0; padding: 0; }
  html, body { width: 712px; height: 1200px; overflow: hidden; }
  body {
    background: var(--page-bg);
    font-family: "Source Sans 3", "Helvetica Neue", Arial, sans-serif;
    color: var(--ink);
    position: relative;
  }
  .site-header .brand {
    position: absolute; left: 52px; top: 18px;
    color: var(--brand-blue);
  }
  .brand-name { font-size: 33px; font-weight: 700; line-height: 1; letter-spacing: -0.5px; }
  .brand-tagline { font-size: 13px; font-weight: 600; color: var(--brand-blue-light); line-height: 1; margin-top: 1px; }
  .social-links { position: absolute; top: 33px; left: 559px; display: flex; gap: 13px; list-style: none; }
  .social-links li { width: 24px; height: 24px; border-radius: 50%; }
  .social-links .s1 { background: var(--social-1); }
  .social-links .s2 { background: var(--social-2); }
  .social-links .s3 { background: var(--social-3); }

  .panel {
    position: absolute; left: 52px; top: 73px; width: 608px; height: 1066px;
    background: var(--panel-bg); border: 1px solid var(--panel-border);
  }
  .main-nav { position: absolute; left: 0; top: 0; width: 100%; height: 45px; }
  .main-nav a {
    position: absolute; top: 12px; height: 24px; line-height: 24px;
    font-size: 14px; font-weight: 600; color: var(--ink-faint); text-decoration: none;
  }
  .main-nav a.active { background: var(--nav-active); color: #7fb3c7; padding: 0 15px; }

  .hero {
    position: absolute; left: 0; top: 45px; width: 606px; height: 325px;
    background: linear-gradient(180deg, #a89580 0%, #6e5a48 25%, #3a2e28 55%, #141218 100%);
  }
  .search-box {
    position: absolute; left: 93px; top: 120px; width: 451px; height: 110px;
    background: var(--search-blue);
  }
  .search-box h2 {
    position: absolute; left: 34px; top: 12px;
    color: #fff; font-size: 32px; font-weight: 700; letter-spacing: 0.3px;
  }
  .search-input {
    position: absolute; left: 34px; top: 53px; width: 290px; height: 37px;
    background: #fff; border: 1px solid #cfd8dc; padding-left: 19px;
    font-size: 13px; line-height: 35px; color: var(--ink-faint);
  }
  .search-go {
    position: absolute; left: 338px; top: 53px; width: 82px; height: 37px;
    background: var(--search-blue-pale); color: var(--search-blue);
    font-size: 25px; font-weight: 700; text-align: center; line-height: 37px;
  }

  .bar-title {
    position: absolute; left: 22px; top: 386px;
    font-size: 26px; font-weight: 600; color: var(--brand-blue);
  }
  .card { position: absolute; background: #fff; border: 1px solid var(--panel-border); }
  .card svg { display: block; width: 100%; height: 100%; }
  .card-attendance { left: 22px; top: 437px; width: 241px; height: 216px; background: var(--teal); border: none; }
  .card-ratio { left: 298px; top: 437px; width: 284px; height: 216px; }
  .card-other { left: 22px; top: 673px; width: 241px; height: 137px; }
  .card-line { left: 298px; top: 673px; width: 284px; height: 118px; }
  svg text { font-family: "Source Sans 3", "Helvetica Neue", Arial, sans-serif; }

  .specials { position: absolute; left: 29px; top: 836px; width: 551px; }
  .specials h3 {
    font-size: 21px; font-weight: 400; color: var(--ink-soft);
    padding-bottom: 6px; border-bottom: 1px solid #e2e2e2;
  }
  .specials ul { list-style: none; margin-top: 9px; }
  .specials li { font-size: 13.5px; line-height: 21.5px; color: var(--ink); }
  .specials li.headline { font-weight: 700; }

  .site-footer {
    position: absolute; left: 0; top: 1155px; width: 712px; text-align: center;
    font-size: 10.5px; color: var(--ink);
  }
  .site-footer .brand-link { color: var(--brand-blue); }
</style>
</head>
<body>
  <header class="site-header">
    <div class="brand">
      <div class="brand-name">Fim-Bosk</div>
      <div class="brand-tagline">Find bars near you</div>
    </div>
    <ul class="social-links" aria-label="Social links">
      <li class="s1"></li><li class="s2"></li><li class="s3"></li>
    </ul>
  </header>

  <main class="panel">
    <nav class="main-nav">
      <a class="active" href="#" style="left:6px">Home</a>
      <a href="#" style="left:89px">Blog</a>
      <a href="#" style="left:150px">Contact us</a>
      <a href="#" style="left:248px">About us</a>
    </nav>

    <section class="hero" role="img" aria-label="Crowd of people at a packed party with hands raised under stage lights">
      <div class="search-box">
        <h2>FIND A BAR</h2>
        <div class="search-input">TYPE A BAR NEAR YOU</div>
        <div class="search-go">GO</div>
      </div>
    </section>

    <h1 class="bar-title">Marlowe Night Club :</h1>

    <div class="card card-attendance">
      <svg viewBox="0 0 257 231" aria-label="Bar attendance chart">
        <text x="128" y="21" text-anchor="middle" fill="#fff" font-size="12">BAR ATTENDANCE</text>
        <g stroke="#ffffff" stroke-opacity="0.15" stroke-width="1">
          <line x1="32" y1="67" x2="225" y2="67"/>
          <line x1="32" y1="98" x2="225" y2="98"/>
          <line x1="32" y1="129" x2="225" y2="129"/>
          <line x1="32" y1="160" x2="225" y2="160"/>
          <line x1="32" y1="192" x2="225" y2="192"/>
          <line x1="32" y1="67" x2="32" y2="192"/>
          <line x1="65" y1="67" x2="65" y2="192"/>
          <line x1="98" y1="67" x2="98" y2="192"/>
          <line x1="130" y1="67" x2="130" y2="192"/>
          <line x1="163" y1="67" x2="163" y2="192"/>
          <line x1="196" y1="67" x2="196" y2="192"/>
          <line x1="225" y1="67" x2="225" y2="192"/>
        </g>
        <g fill="#ffffff" fill-opacity="0.45" font-size="7">
          <text x="12" y="100">30 K</text>
          <text x="12" y="131">20 K</text>
          <text x="12" y="162">10 K</text>
          <text x="65" y="206" text-anchor="middle">JAN</text>
          <text x="95" y="206" text-anchor="middle">FEB</text>
          <text x="128" y="206" text-anchor="middle">MAR</text>
          <text x="158" y="206" text-anchor="middle">APR</text>
          <text x="191" y="206" text-anchor="middle">MAY</text>
          <text x="225" y="206" text-anchor="middle">JUN</text>
        </g>
        <polyline points="32,193 65,178 95,182 128,127" fill="none" stroke="#7fd8ea" stroke-width="2"/>
        <polyline points="128,127 158,108 191,97 225,114" fill="none" stroke="#ffffff" stroke-width="2.5"/>
        <circle cx="128" cy="127" r="13" fill="#ffffff" fill-opacity="0.3"/>
        <g fill="#ffffff">
          <circle cx="32" cy="193" r="4"/><circle cx="65" cy="178" r="4"/>
          <circle cx="95" cy="182" r="4"/><circle cx="128" cy="127" r="4.5"/>
          <circle cx="158" cy="108" r="4"/><circle cx="191" cy="97" r="4"/>
          <circle cx="225" cy="114" r="4"/>
        </g>
      </svg>
    </div>

    <div class="card card-ratio">
      <svg viewBox="0 0 304 232" aria-label="Guy to girl ratio chart">
        <text x="152" y="27" text-anchor="middle" fill="#777" font-size="13">GUY/GIRL RATIO</text>
        <path d="M106,55 A74,74 0 1 0 131.3,198.5" fill="none" stroke="var(--orange)" stroke-width="9"/>
        <path d="M131.3,198.5 A74,74 0 0 0 179.7,135.4" fill="none" stroke="var(--sky)" stroke-width="12"/>
        <circle cx="106" cy="129" r="49" fill="var(--ratio-core)"/>
        <text x="106" y="139" text-anchor="middle" fill="#fff" font-size="28">Ratio</text>
        <text x="116" y="201" fill="#fff" font-size="7">60%</text>
        <text x="169" y="165" fill="#fff" font-size="7" transform="rotate(-60 169 165)">25%</text>
        <rect x="224" y="62" width="15" height="15" fill="var(--orange)"/>
        <text x="246" y="74" fill="#999" font-size="12">Girls</text>
        <rect x="224" y="90" width="15" height="15" fill="var(--sky)"/>
        <text x="246" y="102" fill="#999" font-size="12">Guys</text>
      </svg>
    </div>

    <div class="card card-other">
      <svg viewBox="0 0 257 147" aria-label="Other information">
        <text x="124" y="26" text-anchor="middle" fill="#777" font-size="13">OTHER INFORMATION</text>
        <text x="31" y="57" fill="#555" font-size="9.5">IS THERE ADMITTANCE FEE ?</text>
        <rect x="31" y="70" width="47" height="14" rx="7" fill="var(--teal)"/>
        <text x="39" y="80" fill="#fff" font-size="8.5" font-weight="600">Yeah</text>
        <circle cx="71" cy="77" r="5.5" fill="#fff"/>
        <text x="31" y="110" fill="#555" font-size="9.5">IS THERE BAR RAID ?</text>
        <rect x="31" y="121" width="47" height="14" rx="7" fill="var(--red)"/>
        <circle cx="38" cy="128" r="5.5" fill="#fff"/>
        <text x="47" y="131" fill="#fff" font-size="8.5" font-weight="600">Nope</text>
      </svg>
    </div>

    <div class="card card-line">
      <svg viewBox="0 0 304 127" aria-label="The length of the line">
        <text x="158" y="26" text-anchor="middle" fill="#777" font-size="13">THE LENGTH OF THE LINE</text>
        <g fill="#fff" stroke="#aaa" stroke-width="1">
          <rect x="10.5" y="49.5" width="18" height="18"/>
          <rect x="125.5" y="49.5" width="18" height="18"/>
          <rect x="216.5" y="49.5" width="18" height="18"/>
          <rect x="10.5" y="72.5" width="18" height="18"/>
          <rect x="125.5" y="72.5" width="18" height="18"/>
        </g>
        <path d="M129,58 L133,62 L140,54" fill="none" stroke="#1fb89a" stroke-width="2.5"/>
        <g fill="#555" font-size="11">
          <text x="34" y="63">Really Short</text>
          <text x="149" y="63">Medium</text>
          <text x="241" y="61">Really Long</text>
          <text x="34" y="86">Short</text>
          <text x="149" y="86">Long</text>
        </g>
      </svg>
    </div>

    <section class="specials">
      <h3>DRINK SPECIALS :</h3>
      <ul>
        <li class="headline">WINE NIGHT!</li>
        <li>$8 BOTTLES OF GALLOWMERE WINE</li>
        <li>$8 BOTTLES OF CHAMPAGNE</li>
        <li>$2 TRESK PALE BOTTLES</li>
        <li>$2 WELLS</li>
        <li>$2 TRESK PALE BOTTLES</li>
        <li>$2 WELLS</li>
      </ul>
    </section>
  </main>

  <footer class="site-footer"><span class="brand-link">Fim-Bosk</span> - Copyright 2013 | All rights reserved.</footer>
</body>
</html>
```